Need App for Impact Related Events

My app is to help with internal events. When you enter the prompted event code the next screen shows you everyone currently at the event. It will give you the ability to Start a conversation with someone you met at that event, or signal it is your turn to send a message. The next screen is a message thread with that person. I am looking for a design that incorporates the colors and ‘feel good’ emotion of our logo. I have pieced together a pretty good interpretation of what I’m looking for in the attached mockup by slicing and dicing designs. I also attached our logo mascot.Screens (see attached mockups)

Note 1: I do not like the picture on the screen used in screen one because it makes it seem like a dating app. I attached an alternative photo that can be used or present different ideas.

Note 2: On the login/signup screen (screen 2) I need an additional first and last name for login, you can try to fit this on one login screen or present a two step signup screen where that is presented in the second screen.

READ MOCKUP GUIDELINES UNDER Must Haves

Target Market(s)

People attending internal social impact events

Industry/Entity Type

Charity

Font styles to use
Sans Serif

Colors
86cfc6

Requirements
Must have
• Follow the screen mockups attached to project
• PLEASE READ
• I have provided a relatively close design of what I’m looking for in the mockups. Some screens need to be followed more closely to my design mockup than other. I have listed a guide below how how closely you should follow my mockup design exactly. Overall I would like to see some ideas of incorporating a few accent colors so it doesn’t appear SO Blue. I also attached some app inspiration designs I found from around the web
• Screen Mockup Guideline Follow %
• Screen 1: 65% - mostly on target, would like to see ways to make it not SO Blue and possibly creative places to add some explainer text describing the app
• Screen 2: 50% - general design idea is here, but more open
• Screen 3: 35% - a lot more room for design influence
• Screen 4: 70% - mostly on target, a little room for design influence/color scheme ideas
• Screen 5-6: 25% - a lot of room for design change/ideas/influence
• Screen 7-8: 80% - already very close to what I need, maybe open to slight sizing and color scheme ideas
• Screen 9: 15% - the most open for influence, only the general functionality of the screen is communicated here
Nice to have
• Please Read Mockup Guideline above. In large part I am looking for something to use some nice accent colors so it is not overwhelmingly blue and bring the whole design into a seamless style.
Should not have

```html
<!DOCTYPE html>
<html lang="en">
<head>
<meta charset="utf-8">
<title>Who you've met so far</title>
<link rel="stylesheet" href="https://fonts.googleapis.com/css2?family=Work+Sans:wght@200;300;400;600;700&display=swap">
<style>
  :root {
    --page-bg: #eceef0;
    --screen-bg: #ffffff;
    --teal: #37c9c6;
    --ink: #2b2720;
    --muted: #a9a9a9;
    --avatar-1: #8a9aa8;
    --avatar-2: #8c5a45;
    --avatar-3: #b59a86;
    --avatar-4: #4a3a34;
    --avatar-5: #a87a6a;
  }
  * { box-sizing: border-box; margin: 0; padding: 0; }
  html, body {
    width: 1200px; height: 1126px; overflow: hidden;
    background: var(--page-bg);
    font-family: "Work Sans", sans-serif;
    color: var(--ink);
  }
  .app-screen {
    position: absolute; left: 380px; top: 88px;
    width: 440px; height: 950px;
    background: var(--screen-bg);
    border-radius: 44px;
    box-shadow: 0 20px 50px rgba(0,0,0,0.08);
    padding: 36px 34px 36px;
    overflow: hidden;
  }
  .top-bar { display: flex; justify-content: space-between; align-items: flex-start; height: 110px; }
  .back-link { margin-top: 86px; }
  .top-right { display: flex; flex-direction: column; align-items: flex-end; gap: 20px; }
  .brand { display: flex; align-items: center; gap: 8px; font-weight: 700; font-size: 20px; color: var(--ink); }
  .brand-dot { width: 14px; height: 14px; border-radius: 50%; background: var(--teal); }
  .page-title { margin-top: 18px; font-size: 42px; line-height: 1.05; letter-spacing: -1px; }
  .page-title .light { display: block; font-weight: 200; }
  .page-title .bold { display: block; font-weight: 700; }
  .search {
    margin-top: 26px; display: flex; align-items: center; justify-content: space-between;
    border-bottom: 1.5px solid var(--teal); padding-bottom: 10px;
  }
  .search-label { font-size: 13px; font-style: italic; font-weight: 300; color: var(--muted); }
  .contact-list { list-style: none; margin-top: 22px; }
  .contact {
    display: flex; align-items: center; gap: 18px;
    height: 100px;
  }
  .avatar { width: 72px; height: 72px; border-radius: 50%; flex: none; }
  .contact-info { flex: 1; min-width: 0; }
  .contact-name { font-size: 15px; font-weight: 700; white-space: nowrap; }
  .contact-place { font-size: 10px; color: var(--muted); margin-top: 3px; white-space: nowrap; }
  .contact-action { flex: none; display: flex; align-items: center; }
  .last-message { font-size: 14px; color: var(--muted); font-weight: 400; white-space: nowrap; }
  .load-more {
    display: block; margin: 14px 0 0 auto;
    width: 150px; height: 42px; border-radius: 22px;
    border: 1.5px solid var(--teal); background: none;
    color: var(--teal); font-family: inherit; font-size: 13px; font-weight: 600;
  }
</style>
</head>
<body>
<main class="app-screen">
  <header class="top-bar">
    <svg class="back-link" width="30" height="24" viewBox="0 0 30 24" aria-label="Back">
      <path d="M28 12H3M12 3 3 12l9 9" fill="none" stroke="var(--teal)" stroke-width="2.5" stroke-linecap="round" stroke-linejoin="round"/>
    </svg>
    <div class="top-right">
      <svg width="22" height="22" viewBox="0 0 24 24" aria-label="Settings">
        <g fill="var(--teal)">
          <circle cx="12" cy="12" r="6"/>
          <rect x="10" y="1" width="4" height="22" rx="1.5"/>
          <rect x="1" y="10" width="22" height="4" rx="1.5"/>
          <rect x="10" y="1" width="4" height="22" rx="1.5" transform="rotate(45 12 12)"/>
          <rect x="10" y="1" width="4" height="22" rx="1.5" transform="rotate(-45 12 12)"/>
        </g>
        <circle cx="12" cy="12" r="2.6" fill="#fff"/>
      </svg>
      <div class="brand"><span class="brand-dot"></span>Hivewell</div>
    </div>
  </header>

  <h1 class="page-title"><span class="light">Who you've</span><span class="bold">met so far</span></h1>

  <label class="search">
    <span class="search-label">Search names</span>
    <svg width="22" height="12" viewBox="0 0 22 12" aria-hidden="true">
      <circle cx="5" cy="6" r="4" fill="none" stroke="var(--teal)" stroke-width="1.5"/>
      <path d="M9 6h12M17 6v4M20 6v3" fill="none" stroke="var(--teal)" stroke-width="1.5"/>
    </svg>
  </label>

  <ul class="contact-list">
    <li class="contact">
      <div class="avatar" style="background:var(--avatar-1)" role="img" aria-label="Profile photo of Dean Falkner"></div>
      <div class="contact-info"><p class="contact-name">Dean Falkner</p><p class="contact-place">United States</p></div>
      <div class="contact-action">
        <svg width="26" height="24" viewBox="0 0 26 24" aria-label="Start conversation"><path d="M3 3h20v14H11l-5 4v-4H3z" fill="none" stroke="var(--teal)" stroke-width="2" stroke-linejoin="round"/></svg>
      </div>
    </li>
    <li class="contact">
      <div class="avatar" style="background:var(--avatar-2)" role="img" aria-label="Profile photo of Rosa Whitlock"></div>
      <div class="contact-info"><p class="contact-name">Rosa Whitlock</p><p class="contact-place">United States</p></div>
      <div class="contact-action">
        <svg width="24" height="24" viewBox="0 0 24 24" aria-label="Your turn to reply"><path d="M4 9 9 4h7M20 15l-5 5H8M12 1l4 3-4 3M12 17l-4 3 4 3" fill="none" stroke="var(--ink)" stroke-width="2.4" stroke-linejoin="round"/></svg>
      </div>
    </li>
    <li class="contact">
      <div class="avatar" style="background:var(--avatar-3)" role="img" aria-label="Profile photo of Tessa Morland"></div>
      <div class="contact-info"><p class="contact-name">Tessa Morland</p><p class="contact-place">United States</p></div>
      <div class="contact-action">
        <svg width="26" height="24" viewBox="0 0 26 24" aria-label="Start conversation"><path d="M3 3h20v14H11l-5 4v-4H3z" fill="none" stroke="var(--teal)" stroke-width="2" stroke-linejoin="round"/></svg>
      </div>
    </li>
    <li class="contact">
      <div class="avatar" style="background:var(--avatar-4)" role="img" aria-label="Profile photo of Nadia Fenwick"></div>
      <div class="contact-info"><p class="contact-name">Nadia Fenwick</p><p class="contact-place">United States</p></div>
      <div class="contact-action"><span class="last-message">Great Idea......</span></div>
    </li>
    <li class="contact">
      <div class="avatar" style="background:var(--avatar-5)" role="img" aria-label="Profile photo of Owen Hartley"></div>
      <div class="contact-info"><p class="contact-name">Owen Hartley</p><p class="contact-place">United States</p></div>
      <div class="contact-action"><span class="last-message">Awesome Meeting......</span></div>
    </li>
  </ul>

  <button class="load-more" type="button">Load more....</button>
</main>
</body>
</html>
```